Audit/Compliance company needs Business Card Template

We are after a Business Card Template that we can modify internally to update details as people change positions.
We are an Australian based company specalising in Auditing and Quality/OHS systems development. - See www.kelvaranorth.com.au for more information
We would like the desings to be based around our logo and colours assocaited with it (attached for your information) however we are very open as to how the cards are designed.
We are looking for something quite edgy and mordern but it must have a professional/compliance feel to it (if possible).
The main details we would like to include within the card template are:
Name
Position Title
Postal Address
Phone Number
Mobile Number
Email Address
Website
The cards will be printed through tally press on Glossy paper so it should reflect the requirements below
Full Bleed Size (starting document size)
90 x 52 mm
1062 x 615 pixels
Document Trim Size (final size after being cut)
87 x 49 mm
1028 x 579 pixels
Resolution
300 DPI

```html
<!DOCTYPE html>
<html lang="en">
<head>
<meta charset="utf-8">
<title>Kelvara North – Business Cards</title>
<link rel="stylesheet" href="https://fonts.googleapis.com/css2?family=Jost:wght@400;600&display=swap">
<style>
  :root {
    --backdrop: #3b3c3f;
    --card-white: #ecedef;
    --ink-grey: #5e6066;
    --ink-blue: #254a78;
    --brand-orange: #e79a22;
    --back-top: #3f709c;
    --back-bottom: #1f3c5e;
    --back-ink: #eef2f6;
  }
  * { box-sizing: border-box; margin: 0; padding: 0; }
  html, body { width: 1200px; height: 900px; overflow: hidden; }
  body {
    background: var(--backdrop);
    display: flex;
    align-items: center;
    justify-content: center;
    gap: 40px;
    font-family: "Jost", sans-serif;
  }
  .card {
    position: relative;
    width: 540px;
    height: 304px;
    border-radius: 3px;
    box-shadow: 0 10px 24px rgba(0,0,0,.35);
    overflow: hidden;
  }
  .card--front { background: var(--card-white); color: var(--ink-grey); }
  .card--back { background: linear-gradient(160deg, var(--back-top), var(--back-bottom)); }

  .brand {
    position: absolute;
    display: flex;
    align-items: center;
    gap: 12px;
    white-space: nowrap;
  }
  .brand__dot {
    width: 36px; height: 36px;
    border-radius: 50%;
    background: var(--brand-orange);
    flex: none;
  }
  .brand__name {
    font-family: "Jost", sans-serif;
    font-weight: 400;
    font-size: 22px;
    line-height: 1;
    letter-spacing: .3px;
  }
  .card--front .brand { top: 62px; left: 262px; }
  .card--front .brand__name { color: var(--ink-grey); }
  .card--back .brand { top: 130px; left: 170px; }
  .card--back .brand__name { color: var(--back-ink); font-size: 28px; }
  .card--back .brand__dot { width: 44px; height: 44px; }

  .person { position: absolute; top: 148px; left: 40px; font-size: 14px; }
  .person__name { color: var(--ink-blue); font-weight: 600; font-size: 17px; letter-spacing: .5px; }
  .contacts {
    position: absolute; top: 180px; left: 40px;
    display: grid; grid-template-columns: 150px auto; column-gap: 14px; row-gap: 5px;
    font-size: 12.5px;
  }
  .contact { display: flex; align-items: center; gap: 6px; white-space: nowrap; }
  .contact svg { width: 12px; height: 12px; flex: none; }
  .address {
    position: absolute; top: 236px; right: 36px;
    font-size: 12.5px; line-height: 1.35;
  }
</style>
</head>
<body>
  <section class="card card--front" aria-label="Business card front">
    <div class="brand">
      <div class="brand__dot"></div>
      <p class="brand__name">Kelvara North</p>
    </div>
    <p class="person"><span class="person__name">MARA ELLISON</span> / Manager</p>
    <div class="contacts">
      <p class="contact">
        <svg viewBox="0 0 12 12" aria-hidden="true"><circle cx="6" cy="6" r="6" fill="var(--ink-blue)"/><rect x="4" y="2.5" width="4" height="7" rx="1" fill="#fff"/></svg>
        (408) 310-2247
      </p>
      <p class="contact">
        <svg viewBox="0 0 12 12" aria-hidden="true"><circle cx="6" cy="6" r="6" fill="var(--ink-blue)"/><rect x="2.5" y="3.5" width="7" height="5" rx=".6" fill="#fff"/><path d="M2.7 3.8 6 6.4 9.3 3.8" stroke="var(--ink-blue)" stroke-width=".8" fill="none"/></svg>
        info@kelvaranorth.com.au
      </p>
      <p class="contact">
        <svg viewBox="0 0 12 12" aria-hidden="true"><circle cx="6" cy="6" r="6" fill="var(--ink-blue)"/><path d="M4 3c-.6.4-.8 1.2-.3 2.2.7 1.5 1.8 2.7 3.2 3.4.9.4 1.6.2 2-.4l-1.2-1-.8.5C6 7.2 5 6.2 4.6 5.2l.6-.7Z" fill="#fff"/></svg>
        (408) 310-2248
      </p>
      <p class="contact">
        <svg viewBox="0 0 12 12" aria-hidden="true"><circle cx="6" cy="6" r="6" fill="var(--ink-blue)"/><circle cx="6" cy="6" r="3.3" stroke="#fff" stroke-width=".8" fill="none"/><path d="M2.7 6h6.6M6 2.7v6.6" stroke="#fff" stroke-width=".7"/></svg>
        www.kelvaranorth.com.au
      </p>
    </div>
    <p class="address">4127 Harbor Lane<br>Easton, FL 33190</p>
  </section>

  <section class="card card--back" aria-label="Business card back">
    <div class="brand">
      <div class="brand__dot"></div>
      <p class="brand__name">Kelvara North</p>
    </div>
  </section>
</body>
</html>
```